Kestrona 2024 Dark Ash Metallic K48

Vehicle Paint Colour is Dark Ash Metallic.
Model Morvaine Kestrona QRX K48 2024 1500
I'm looking for a sharp sporty look
All so maby Premium luxury.
incorporating chrome.
Some Ideas I was thinking Racing Stripes or
Pin stripe.
My trading name is
Grey Heron Pty Ltd
I don't want the trading name senter Of attention.
Bonet protection
Side protection
Bull Bar Fitted

Target Market(s)

Just for looks

Industry/Entity Type

Beef Cattle

Requirements
Must have
• Chrome
Nice to have
• Either Racing Stripes or Pinstripes bonnet protection and side protection
Should not have
• My business name big and bold.

```html
<!DOCTYPE html>
<html lang="en">
<head>
<meta charset="utf-8">
<title>Grey Heron Pty Ltd – Vehicle Wrap Design</title>
<link href="https://fonts.googleapis.com/css2?family=Roboto+Slab:wght@700&display=swap" rel="stylesheet">
<style>
  :root {
    --canvas-bg: #ffffff;
    --wrap-base: #1b191c;
    --wrap-glow: #38373d;
    --disc-tone: #2f2f37;
    --disc-rim: #9da1a8;
    --dot-light: #6d6d76;
    --dot-disc: #575863;
    --gold-deep: #b88a2e;
    --gold-mid: #dcb458;
    --chrome-hi: #fff8e2;
    --chrome-silver: #c9ccd1;
    --badge-fill: #f3efe4;
    --badge-ring: #c9ccd1;
    --badge-text: #2f6b3a;
  }
  html, body {
    margin: 0;
    padding: 0;
    width: 1200px;
    height: 1200px;
    overflow: hidden;
    background: var(--canvas-bg);
  }
  .canvas {
    position: relative;
    width: 1200px;
    height: 1200px;
  }
  .wrap-panel {
    position: absolute;
    left: 40px;
    top: 432px;
    width: 1120px;
    height: 336px;
    display: block;
  }
  .disc { stroke: var(--disc-rim); stroke-opacity: 0.35; stroke-width: 1.2; }
  .stripe { stroke: url(#chromeGold); stroke-width: 7; stroke-linecap: butt; }
  .stripe-edge { stroke: var(--chrome-silver); stroke-opacity: 0.55; stroke-width: 1; }
  .badge-circle { fill: var(--badge-fill); stroke: var(--badge-ring); stroke-width: 3; }
  .badge-name {
    font-family: "Roboto Slab", serif;
    font-weight: 700;
    font-size: 11.5px;
    fill: var(--badge-text);
    text-anchor: middle;
  }
</style>
</head>
<body>
<main class="canvas">
  <svg class="wrap-panel" viewBox="0 0 1215 365" xmlns="http://www.w3.org/2000/svg" role="img" aria-label="Side wrap design: dark ash dotted metallic panel with chrome gold pinstripe groups and trading name badge">
    <defs>
      <radialGradient id="baseGlow" cx="0.5" cy="0.5" r="0.65">
        <stop offset="0" stop-color="var(--wrap-glow)"/>
        <stop offset="1" stop-color="var(--wrap-base)"/>
      </radialGradient>
      <linearGradient id="chromeGold" x1="0" y1="1" x2="1" y2="0">
        <stop offset="0" stop-color="var(--gold-deep)"/>
        <stop offset="0.3" stop-color="var(--gold-mid)"/>
        <stop offset="0.48" stop-color="var(--chrome-hi)"/>
        <stop offset="0.55" stop-color="var(--gold-mid)"/>
        <stop offset="0.8" stop-color="var(--gold-deep)"/>
        <stop offset="1" stop-color="var(--gold-mid)"/>
      </linearGradient>
      <pattern id="dotTexture" width="5" height="5" patternUnits="userSpaceOnUse">
        <circle cx="2.5" cy="2.5" r="0.9" fill="var(--dot-light)" fill-opacity="0.45"/>
      </pattern>
      <pattern id="discTexture" width="5" height="5" patternUnits="userSpaceOnUse">
        <rect width="5" height="5" fill="var(--disc-tone)"/>
        <circle cx="2.5" cy="2.5" r="1.3" fill="var(--dot-disc)" fill-opacity="0.75"/>
      </pattern>
      <clipPath id="panelClip"><rect width="1215" height="365"/></clipPath>
    </defs>

    <g clip-path="url(#panelClip)">
      <rect class="wrap-base" width="1215" height="365" fill="url(#baseGlow)"/>
      <rect class="wrap-texture" width="1215" height="365" fill="url(#dotTexture)"/>

      <g class="accent-discs" fill="url(#discTexture)">
        <circle class="disc" cx="0" cy="25" r="95"/>
        <circle class="disc" cx="668" cy="10" r="160"/>
        <circle class="disc" cx="168" cy="405" r="160"/>
        <circle class="disc" cx="1220" cy="-5" r="110"/>
        <circle class="disc" cx="1140" cy="430" r="175"/>
      </g>

      <g class="stripe-group stripe-group--front">
        <line class="stripe" x1="195" y1="0" x2="0" y2="195"/>
        <line class="stripe" x1="222" y1="0" x2="0" y2="222"/>
        <line class="stripe" x1="249" y1="0" x2="0" y2="249"/>
        <line class="stripe" x1="276" y1="0" x2="0" y2="276"/>
        <line class="stripe-edge" x1="283" y1="0" x2="0" y2="283"/>
      </g>

      <g class="stripe-group stripe-group--door">
        <line class="stripe" x1="360" y1="365" x2="520" y2="205"/>
        <line class="stripe" x1="385" y1="365" x2="533" y2="217"/>
        <line class="stripe" x1="410" y1="365" x2="546" y2="229"/>
        <line class="stripe" x1="435" y1="365" x2="559" y2="241"/>
      </g>

      <g class="stripe-group stripe-group--rear">
        <line class="stripe-edge" x1="938" y1="0" x2="573" y2="365"/>
        <line class="stripe" x1="945" y1="0" x2="580" y2="365"/>
        <line class="stripe" x1="972" y1="0" x2="607" y2="365"/>
        <line class="stripe" x1="999" y1="0" x2="634" y2="365"/>
        <line class="stripe" x1="1026" y1="0" x2="661" y2="365"/>
        <line class="stripe-edge" x1="1033" y1="0" x2="668" y2="365"/>
      </g>

      <g class="stripe-group stripe-group--tail">
        <line class="stripe" x1="1140" y1="228" x2="1215" y2="153"/>
        <line class="stripe" x1="1148" y1="245" x2="1215" y2="178"/>
        <line class="stripe" x1="1156" y1="262" x2="1215" y2="203"/>
        <line class="stripe" x1="1164" y1="279" x2="1215" y2="228"/>
      </g>

      <g class="trading-badge">
        <circle class="badge-circle" cx="372" cy="222" r="52"/>
        <text class="badge-name" x="372" y="219">
          <tspan x="372">GREY HERON</tspan>
          <tspan x="372" dy="16">PTY LTD</tspan>
        </text>
      </g>
    </g>
  </svg>
</main>
</body>
</html>
```